Stylish High End Wedding Videography/Films Website (BDMR)

We need a modern and high-end website look for our wedding video and films business. We films weddings all over the United Kingdom and at European destinations so need something to reflect our work. The website should be visually stunning with images and videos being the focal point as this is what our services are;

I have uploads of some items I like and the features the site needs to have. These have been taken from other websites using standout features.

We need the following pages;

1 - Homepage
2 - Films Index Page
3 - Individual Films Page
4 - Prices / Collection Page
5 - Reviews
6 - Options
7 - About
8 - Contact
9 - Blog Index
10 - Blog Page

All pages must be consistent so have a similar style.

Pages on menu:
Films
Prices
Reviews
Options
About
Contact

We require a responsive look too. Over 90% of our visitors access the website via their mobile devices.

Please use the colours from our logo to incorporate into the website.

Target Market(s)

Wedding Couples

Industry/Entity Type

Wedding Photography

Number of Pages Required

5+ page

Font styles to use
Sans Serif
Script

Requirements
Must have
• The logo must be in the centre of the menu at the top.

Social icons at the bottom of the page.

Use only two fonts including Lore which is supplied
Nice to have
• Different video for each page on the top header. This will play behind the menu.

```html
<!DOCTYPE html>
<html lang="en">
<head>
<meta charset="utf-8">
<title>BDMR Wedding Films</title>
<link rel="stylesheet" href="https://fonts.googleapis.com/css2?family=Josefin+Sans:wght@300;400;600&family=Yellowtail&display=block">
<style>
:root{
  --gold:#b8995a;
  --text:#7a7a7a;
  --dark:#3d3d3d;
  --paper:#ffffff;
  --footer:#efeeec;
  --line:#dcdad5;
  --script:"Yellowtail","Brush Script MT","Segoe Script",cursive;
}
*{margin:0;padding:0;box-sizing:border-box}
html,body{width:1200px;height:3940px;overflow:hidden}
body{background:var(--paper);font-family:"Josefin Sans",sans-serif;color:var(--text);font-weight:300}
.photo{display:block}
/* hero */
.hero{position:relative;height:748px;background:linear-gradient(180deg,#1e3a7a 0%,#4f78b8 28%,#c9c3b4 52%,#9a9286 72%,#6d665d 100%)}
.nav{position:absolute;top:0;left:0;right:0;height:110px;display:flex;align-items:center;justify-content:center;gap:60px}
.nav-group{display:flex;gap:58px;width:330px}
.nav-group.left{justify-content:flex-end}
.nav a{color:#fff;text-decoration:none;font-size:13px;letter-spacing:3px;text-transform:uppercase;font-weight:400}
.brand{width:200px;text-align:center;color:#fff}
.brand-name{font-size:24px;letter-spacing:4px;font-weight:600}
.brand-sub{font-size:10px;letter-spacing:5px;margin-top:4px}
/* intro */
.intro{height:272px;text-align:center;padding-top:58px}
.script-title{font-family:var(--script);color:var(--gold);font-size:46px;line-height:52px;font-weight:400;font-style:normal}
.intro p{font-size:13px;line-height:21px;width:560px;margin:18px auto 0}
/* grid */
.gallery{display:grid;grid-template-columns:1fr 1fr 1fr;grid-auto-rows:164px;gap:4px;height:500px}
/* about */
.about{height:560px;position:relative}
.section-label{color:var(--gold);font-size:18px;letter-spacing:5px;font-weight:400;text-transform:uppercase}
.about .copy{position:absolute;left:125px;top:130px;width:480px}
.about .copy p{font-size:13px;line-height:21px;margin-top:20px}
.about .portrait{position:absolute;left:660px;top:120px;width:410px;height:210px}
/* feature */
.feature{position:relative;height:640px;background:linear-gradient(180deg,#f3dcae 0%,#e9c585 30%,#a2874f 60%,#4f4a2e 85%,#34321f 100%)}
.feature-quote{position:absolute;left:125px;top:160px;width:380px;font-family:var(--script);color:#fff;font-size:21px;line-height:27px;font-weight:400}
/* text section */
.story{height:700px;position:relative}
.story .section-label{position:absolute;top:110px;left:0;right:0;text-align:center;font-size:28px;letter-spacing:8px}
.story .cols{position:absolute;top:180px;left:125px;right:125px;display:grid;grid-template-columns:1fr 1fr;gap:70px}
.story p{font-size:13px;line-height:21px;margin-bottom:20px}
.mark{position:absolute;left:0;right:0;top:560px;text-align:center;color:var(--gold);font-size:30px;letter-spacing:8px;font-weight:400}
/* footer */
.footer{background:var(--footer);height:520px;position:relative}
.strip{display:grid;grid-template-columns:repeat(7,1fr);gap:4px;height:150px;margin:0 120px;padding-top:0}
.strip .photo{height:150px}
.handle{background:#2f2f2f;display:flex;align-items:center;justify-content:center;color:#fff;font-size:12px;letter-spacing:1px}
.foot-cols{position:absolute;top:220px;left:125px;display:flex;gap:120px}
.foot-head{color:var(--gold);font-size:12px;letter-spacing:3px;text-transform:uppercase;margin-bottom:24px;font-weight:400}
.links{display:grid;grid-template-columns:110px 110px;row-gap:16px}
.links a,.foot-item{color:var(--text);text-decoration:none;font-size:12px}
.foot-item{display:flex;align-items:center;gap:12px;margin-bottom:16px}
.dot{width:14px;height:14px;border-radius:50%;background:var(--gold);display:inline-block}
.foot-bottom{position:absolute;left:125px;right:125px;bottom:30px;display:flex;justify-content:space-between;align-items:center;border-top:1px solid var(--line);padding-top:18px}
.copyright{font-size:10px;letter-spacing:3px;text-transform:uppercase}
.badge{width:110px;height:22px;background:#f2d500}
</style>
</head>
<body>
<header class="hero">
  <div role="img" aria-label="Wedding couple dancing in a grand colonnaded piazza under a blue sky" style="position:absolute;inset:0"></div>
  <nav class="nav">
    <div class="nav-group left"><a href="#">Films</a><a href="#">Prices</a><a href="#">Reviews</a></div>
    <div class="brand"><div class="brand-name">BDMR</div><div class="brand-sub">WEDDING FILMS</div></div>
    <div class="nav-group"><a href="#">Options</a><a href="#">About</a><a href="#">Contact</a></div>
  </nav>
</header>

<section class="intro">
  <h1 class="script-title">We film weddings in a fun and natural way.<br>All weddings are totally unique to the couple.</h1>
  <p>Ben Delamere is a wedding filmmaker based in the North East of England. If you are looking for a wedding film that feels honest, relaxed and true to you, get in touch.</p>
</section>

<section class="gallery">
  <div class="photo" role="img" aria-label="Couple embracing in a golden field" style="background:linear-gradient(135deg,#c9a15e,#6e5a35)"></div>
  <div class="photo" role="img" aria-label="Couple at sunset by the sea" style="background:linear-gradient(180deg,#3d6f9e,#e79a55)"></div>
  <div class="photo" role="img" aria-label="Bride holding a bouquet" style="background:linear-gradient(135deg,#8d7a68,#dcd2c6)"></div>
  <div class="photo" role="img" aria-label="Couple close together outdoors" style="background:linear-gradient(135deg,#7f8c57,#3e4a2c)"></div>
  <div class="photo" role="img" aria-label="Couple kissing in soft light" style="background:linear-gradient(135deg,#5a463c,#b39b86)"></div>
  <div class="photo" role="img" aria-label="Couple on a hillside with cloudy sky" style="background:linear-gradient(180deg,#a9b3bd,#7c7466)"></div>
  <div class="photo" role="img" aria-label="Couple on a beach" style="background:linear-gradient(180deg,#bfc6c9,#8c8472)"></div>
  <div class="photo" role="img" aria-label="Ceremony under a floral arch" style="background:linear-gradient(135deg,#d4c8ba,#8e857b)"></div>
  <div class="photo" role="img" aria-label="Couple portrait in a doorway" style="background:linear-gradient(135deg,#6a5444,#c2ab90)"></div>
</section>

<section class="about">
  <div class="copy">
    <h2 class="section-label">Ben Delamere</h2>
    <p>I'm a filmmaker who loves documenting couples. Ever since my first day filming weddings I have been hooked, and I now travel across the North East of England and beyond to capture every moment.</p>
    <p>I'm still the wedding filmmaker couples trust to tell their story in a natural, relaxed way, and I work hard to keep every film personal, warm and full of the small details that make your day yours.</p>
    <p>Each film is made with care from the first meeting to the final edit, so you can relive your day for years to come.</p>
  </div>
  <div class="portrait" role="img" aria-label="Black and white portrait of the filmmaker" style="background:linear-gradient(135deg,#d8d8d8,#5b5b5b)"></div>
</section>

<section class="feature" role="img" aria-label="Bride and groom embracing on rocks at golden hour">
  <p class="feature-quote">Every love story is unique, and every film should be too. Relaxed, honest and full of feeling, your wedding film is a memory you will treasure for the rest of your lives together.</p>
</section>

<section class="story">
  <h2 class="section-label">Lorem Ipsum</h2>
  <div class="cols">
    <div>
      <p>Lorem ipsum dolor sit amet, consectetur adipiscing elit. Vivamus et tellus vitae sapien fringilla luctus. Donec ac magna sed ligula pretium finibus, quis viverra nibh ultrices sed.</p>
      <p>Aliquam erat volutpat. Nunc tincidunt ipsum vel erat posuere, at cursus enim feugiat. Sed vitae dui quis mauris euismod tempor. Praesent id lorem eget nisl vulputate sodales non at mauris dolor.</p>
    </div>
    <div>
      <p>Cras in ultrices arcu. Donec vestibulum tempus leo in porta. Mauris ut justo quis nibh tincidunt facilisis, non tincidunt nisi rhoncus eget lacus.</p>
      <p>Praesent lacus dolor, consequat vel faucibus ut, dictum at nulla. Morbi sed dui consectetur in tellus et lorem. Integer vulputate felis vel augue blandit, vitae pretium arcu.</p>
    </div>
  </div>
  <div class="mark">BDMR</div>
</section>

<footer class="footer">
  <div class="strip">
    <div class="photo" role="img" aria-label="Couple dancing" style="background:linear-gradient(135deg,#8b8176,#3f3a35)"></div>
    <div class="photo" role="img" aria-label="Wedding guests" style="background:linear-gradient(135deg,#cfc3b5,#7b6f62)"></div>
    <div class="photo" role="img" aria-label="Couple in an evening scene" style="background:linear-gradient(135deg,#6b5b4d,#2f2a26)"></div>
    <div class="handle">@bdmrweddingfilms</div>
    <div class="photo" role="img" aria-label="Wedding table details" style="background:linear-gradient(135deg,#d6ccc0,#9a8e80)"></div>
    <div class="photo" role="img" aria-label="Bride and groom outdoors" style="background:linear-gradient(135deg,#b9b09f,#5d5548)"></div>
    <div class="photo" role="img" aria-label="Couple by a window" style="background:linear-gradient(135deg,#7c4a44,#c6a497)"></div>
  </div>
  <div class="foot-cols">
    <div>
      <h3 class="foot-head">Quick Links</h3>
      <div class="links"><a href="#">Films</a><a href="#">Options</a><a href="#">Prices</a><a href="#">About</a><a href="#">Reviews</a><a href="#">Contact</a></div>
    </div>
    <div style="margin-left:40px">
      <h3 class="foot-head">Contact</h3>
      <div class="foot-item"><svg width="14" height="14" viewBox="0 0 24 24"><path fill="#b8995a" d="M6.6 10.8a15 15 0 0 0 6.6 6.6l2.2-2.2c.3-.3.7-.4 1-.2 1.1.4 2.3.6 3.6.6.6 0 1 .4 1 1V20c0 .6-.4 1-1 1A17 17 0 0 1 3 4c0-.6.4-1 1-1h3.5c.6 0 1 .4 1 1 0 1.3.2 2.5.6 3.6.1.3 0 .7-.2 1z"/></svg>01234 567 890</div>
      <div class="foot-item"><svg width="14" height="14" viewBox="0 0 24 24"><path fill="#b8995a" d="M2 5h20v14H2zm2 2v.5l8 5 8-5V7l-8 5z"/></svg>hello@bdmrfilms.com</div>
    </div>
    <div style="margin-left:40px">
      <h3 class="foot-head">Follow Us</h3>
      <div class="foot-item"><span class="dot"></span>BDMR Films</div>
      <div class="foot-item"><span class="dot"></span>@bdmrweddingfilms</div>
      <div class="foot-item"><span class="dot"></span>BDMR Wedding Films</div>
    </div>
  </div>
  <div class="foot-bottom">
    <span class="copyright">BDMR Wedding Films © 2024</span>
    <span class="badge" role="img" aria-label="Partner badge"></span>
  </div>
</footer>
</body>
</html>
```